Quiet Harbor Health Flyer (new business startup)

One page...clear enough to be read if faxed. This mental health clinic treats depression/anxiety in kids and adults. It also treats opiate and alcohol addiction. It's in downtown Elmira, NY and the owner of the clinic is from Elmira NY, where it's located. This clinic does not take health insurance, so it charges a low rate of $75 a visit once they pay the $125 starting fee.
Updates

Slow in providing feedback

Target Market(s)

doctors offices, new patients

Industry/Entity Type

Doctor

Requirements
Must have
• see microsoft word document. pdf is printed on the company letterhead.
Nice to have
• a simplified map would be nice. if you can include the building it would be a plus. The same two fonts were used in the business cards and letter head (kennedy small caps boo*) and Refrigerator Delux.

```html
<!DOCTYPE html>
<html lang="en">
<head>
<meta charset="utf-8">
<title>Quiet Harbor Health Flyer</title>
<link rel="stylesheet" href="https://fonts.googleapis.com/css2?family=Abel&family=Lato:ital,wght@0,400;1,300&family=Montserrat:wght@800&display=swap">
<style>
  :root {
    --orange: #e86b33;
    --blue: #2aa7de;
    --ink: #2b2b2b;
    --white: #ffffff;
    --page: #f4f4f4;
    --grey-light: #eeeeee;
    --grey-mid: #cfcfcf;
  }
  * { margin: 0; padding: 0; box-sizing: border-box; }
  html, body { width: 1200px; height: 1200px; overflow: hidden; background: var(--page); }
  .flyer {
    position: absolute; left: 198px; top: 30px;
    width: 805px; height: 1140px;
    background: var(--white); overflow: hidden;
    font-family: "Abel", sans-serif; color: var(--ink);
  }
  .abs { position: absolute; }
  .hero-photo {
    left: 0; top: 0; width: 805px; height: 634px;
    background: radial-gradient(ellipse at 62% 30%, #d9d9d9 0%, #efefef 45%, #fafafa 100%);
  }
  .brand { left: 52px; top: 72px; display: flex; align-items: center; gap: 16px; }
  .brand-dot { width: 62px; height: 62px; border-radius: 50%; background: var(--orange); }
  .brand-name {
    font-family: "Montserrat", sans-serif; font-weight: 800;
    font-size: 38px; color: var(--orange); letter-spacing: 0.5px; white-space: nowrap;
  }
  .hours-title {
    left: 0; width: 852px; top: 280px; text-align: center;
    font-family: "Montserrat", sans-serif; font-weight: 800; font-size: 36px; color: var(--orange);
  }
  .hours-text { left: 0; width: 858px; top: 322px; text-align: center; font-size: 38px; }
  .bottom-photo {
    left: 0; top: 634px; width: 805px; height: 437px;
    background: linear-gradient(180deg, #f3f3f6 0%, #ece6e2 45%, #e7e2de 100%);
  }
  .price-card {
    left: 41px; top: 371px; width: 740px; height: 327px;
    background: var(--blue); border-radius: 24px;
  }
  .price-card-dash {
    position: absolute; left: 22px; top: 23px; right: 21px; bottom: 24px;
    border: 1.5px dashed var(--white);
  }
  .clinician-photo {
    left: 30px; top: 345px; width: 195px; height: 353px;
    background: linear-gradient(180deg, #d8e3e6 0%, #eef2f2 50%, #c8d6d4 100%);
    border-radius: 90px 90px 0 0;
  }
  .price-list { left: 277px; top: 430px; width: 474px; color: var(--white); font-size: 31px; line-height: 39px; }
  .price-item + .price-item { margin-top: 10px; }
  .price-row { display: flex; align-items: baseline; }
  .price-leader { flex: 1; border-bottom: 2px dotted var(--white); margin: 0 2px 8px; }
  .ages {
    left: 280px; top: 619px; color: var(--white);
    font-family: "Lato", sans-serif; font-size: 31px; white-space: nowrap;
  }
  .map-area {
    left: 73px; top: 761px; width: 274px; height: 274px; border-radius: 50%;
    background: radial-gradient(circle, #f1f1f1 0%, #e4e6e8 100%);
    border: 3.5px solid var(--orange);
  }
  .building-photo {
    left: 21px; top: 850px; width: 130px; height: 78px;
    background: linear-gradient(180deg, #7a4b3a 0%, #5b3328 100%);
  }
  .conditions-title { left: 388px; top: 772px; font-size: 38px; color: var(--blue); }
  .conditions { font-size: 29px; line-height: 39px; list-style: none; }
  .conditions li::before { content: "\2022"; margin-right: 2px; }
  .conditions .wrap { padding-left: 12px; }
  .conditions-a { left: 388px; top: 827px; }
  .conditions-b { left: 605px; top: 827px; }
  .tagline {
    left: 361px; width: 400px; top: 1030px; text-align: center;
    font-family: "Lato", sans-serif; font-style: italic; font-weight: 300; font-size: 16px; color: #555;
  }
  .footer-band {
    left: 0; top: 1071px; width: 805px; height: 69px; background: var(--orange);
    color: var(--white); font-size: 17px; line-height: 22px; text-align: center;
    display: flex; align-items: center; justify-content: center; padding: 0 40px;
  }
</style>
</head>
<body>
<main class="flyer">
  <div class="abs hero-photo" role="img" aria-label="Soft grey photo of a phrenology head with labelled brain regions"></div>
  <div class="abs bottom-photo" role="img" aria-label="Faded photo of a brick downtown building"></div>

  <header class="abs brand">
    <span class="brand-dot"></span>
    <span class="brand-name">QUIET HARBOR HEALTH</span>
  </header>

  <h2 class="abs hours-title">HOURS:</h2>
  <p class="abs hours-text">Monday and Saturdays 9-4pm</p>

  <section class="abs price-card"><div class="price-card-dash"></div></section>
  <div class="abs clinician-photo" role="img" aria-label="Photo of a clinician in a white coat holding a clipboard"></div>

  <div class="abs price-list">
    <div class="price-item">
      <div>Psychiatric Evaluation</div>
      <div class="price-row"><span>(45min)</span><span class="price-leader"></span><span>$125*</span></div>
    </div>
    <div class="price-item">
      <div>Psychiatric Office Visit</div>
      <div class="price-row"><span>(15min)</span><span class="price-leader"></span><span>$75*</span></div>
    </div>
  </div>
  <p class="abs ages">AGES:&nbsp; 6 YEARS OLD AND UP</p>

  <div class="abs map-area" role="img" aria-label="Simplified street map of downtown with the clinic location marked"></div>
  <div class="abs building-photo" role="img" aria-label="Photo of the brick clinic building"></div>

  <h2 class="abs conditions-title">Conditions Treated:</h2>
  <ul class="abs conditions conditions-a">
    <li>Depression</li>
    <li>PTSD</li>
    <li>Addiction</li>
    <li>Childhood Mood</li>
    <li class="wrap" style="list-style:none">Disorders</li>
  </ul>
  <ul class="abs conditions conditions-b">
    <li>Anxiety</li>
    <li>ADHD</li>
    <li>Bipolar</li>
  </ul>

  <p class="abs tagline">“We work for you, not the insurance companies”</p>

  <footer class="abs footer-band">
    *Although we do not partner with any Health Insurance Companies at this time, a bill will be provided to you at the time of service for you to submit to your insurance company.
  </footer>
</main>
</body>
</html>
```